trading data display webpage

We have build a rough wireframe of the two webpages that we want to display .The two wireframes are attached as a pdf document.
there will be login page. after login , the user will see the index page. that is the first page of the wireframe.

what we are displaying is essentially spread data. we are taking the difference in prices are two places and displaying the data. some calculations are done and is shown in the grid.

below the grid we show the behaviour on a graph. we will use bubble chart. I did not find a sample, hence have thrown in a placeholder.

this is time series data ( changes daily) and hence we need to check the behaviour.

the second wire frame shows how the user will choose the source price points and the destination price points.
we are talking here of natural gas prices hence the reference to source prices and destination prices.

you need to design the page/ pages such that the end-user loves it and is easy to use. the intent here is easy to use and easy to understand.
this will be responsive webpage since the end user will check it out on a tablet or a smartphone.

so if possible tell us how the navigation bar, the button bar, etc should fall when the screen size decreases.

I have uploaded 2 files. one is the wireframe ( pdf document) and second is the logo file.

please also let us know where to place the logo.

Target Market(s)

the target market is traders and data analyst

Industry/Entity Type

Build

Colors

Designer to choose colors to be used in the design.

Requirements
Must have
• 1. design for the web.
2. but think how the design will look when the screen size decreases.
3. tell if possible what screen components to keep and what to hide.

```html
<!DOCTYPE html>
<html lang="en">
<head>
<meta charset="utf-8">
<title>Spreadline – Spread Dashboard</title>
<link href="https://fonts.googleapis.com/css2?family=Open+Sans:wght@600;700&display=swap" rel="stylesheet">
<style>
  :root {
    --page-bg: #e7e7eb;
    --panel-bg: #ffffff;
    --panel-border: #9ccc5a;
    --tab-active: #7fcbea;
    --tab-idle: #ffffff;
    --text-main: #555a60;
    --header-bg: #8fd2ee;
    --row-bg: #f1f1f5;
    --grid-line: #c9c9cf;
    --pill: #e4ce6a;
    --select-bg: #f3f3f5;
    --select-border: #b9b9bd;
    --bar: #0057a8;
    --brand: #0057a8;
    --brand-dot: #f26522;
  }
  * { box-sizing: border-box; margin: 0; padding: 0; }
  html, body { width: 1200px; height: 916px; overflow: hidden; }
  body {
    background: var(--page-bg);
    font-family: "Open Sans", Arial, sans-serif;
    font-weight: 600;
    color: var(--text-main);
    position: relative;
  }
  .brand {
    position: absolute; left: 880px; top: 78px;
    display: flex; align-items: center; gap: 10px;
    font-size: 26px; font-weight: 700; color: var(--brand);
  }
  .brand-dot { width: 18px; height: 18px; border-radius: 50%; background: var(--brand-dot); }

  .region-tabs { position: absolute; left: 96px; top: 124px; display: flex; gap: 3px; }
  .region-tab {
    width: 98px; height: 47px; background: var(--tab-idle);
    display: flex; align-items: center; justify-content: center;
    font-size: 19px; color: var(--text-main);
  }
  .region-tab.is-active { background: var(--tab-active); color: #fff; }

  .dashboard {
    position: absolute; left: 96px; top: 173px; width: 1001px; height: 638px;
    background: var(--panel-bg); border: 1px solid var(--panel-border);
  }
  .index-select {
    position: absolute; top: 18px; width: 188px; height: 41px;
    background: var(--select-bg); border: 1px solid var(--select-border);
    font-size: 14.5px; display: flex; align-items: center; padding-left: 17px;
  }
  .index-select svg { position: absolute; right: 10px; top: 10px; }
  .index-select.source { left: 20px; }
  .index-select.destination { left: 222px; }

  .range-group {
    position: absolute; top: 18px; height: 41px; display: flex;
    border-radius: 12px; overflow: hidden;
  }
  .range-group.short { left: 444px; width: 189px; }
  .range-group.long { left: 645px; width: 190px; }
  .range-btn {
    background: var(--pill); color: #fff; font-size: 14.5px;
    display: flex; align-items: center; justify-content: center;
    border-left: 2px solid #fff;
  }
  .range-btn:first-child { border-left: none; }

  .spread-table {
    position: absolute; left: 29px; top: 101px; width: 944px;
    border-collapse: collapse; font-size: 14.5px;
  }
  .spread-table th {
    background: var(--header-bg); color: #fff; height: 60px;
    text-align: left; padding-left: 32px; font-weight: 600;
    border-left: 1px solid #fff;
  }
  .spread-table th:first-child { border-left: none; }
  .spread-table td {
    background: var(--row-bg); height: 46px; padding-left: 32px;
    border: 1px solid var(--grid-line);
  }
  .spread-table tr:first-child td { height: 49px; }
  .spread-table tr:last-child td { height: 55px; }

  .chart-title { position: absolute; top: 430px; font-size: 18.5px; text-align: center; width: 260px; }
  .chart-title.supply { left: 77px; }
  .chart-title.time { left: 503px; }
  .pie { position: absolute; left: 158px; top: 481px; }
  .bars { position: absolute; left: 511px; top: 476px; }
</style>
</head>
<body>
  <div class="brand"><span class="brand-dot"></span>Spreadline</div>

  <nav class="region-tabs">
    <div class="region-tab is-active">East</div>
    <div class="region-tab">Central</div>
    <div class="region-tab">West</div>
  </nav>

  <main class="dashboard">
    <div class="index-select source">Source Indices
      <svg width="20" height="22" viewBox="0 0 20 22"><path d="M2 9 L10 1 L18 9Z M2 13 L10 21 L18 13Z" fill="#6b6e73"/></svg>
    </div>
    <div class="index-select destination">Destination Indices
      <svg width="20" height="22" viewBox="0 0 20 22"><path d="M2 9 L10 1 L18 9Z M2 13 L10 21 L18 13Z" fill="#6b6e73"/></svg>
    </div>

    <div class="range-group short">
      <div class="range-btn" style="width:67px">5d</div>
      <div class="range-btn" style="width:59px">7d</div>
      <div class="range-btn" style="width:63px">18d</div>
    </div>
    <div class="range-group long">
      <div class="range-btn" style="width:99px">Month</div>
      <div class="range-btn" style="width:91px">Year</div>
    </div>

    <table class="spread-table">
      <colgroup>
        <col style="width:146px"><col style="width:110px"><col style="width:115px"><col style="width:120px"><col style="width:140px"><col style="width:138px"><col style="width:175px">
      </colgroup>
      <thead>
        <tr><th>Spread-name</th><th>avg spd</th><th>+ve prob</th><th>-ve prob</th><th>spike prob</th><th>avg supply</th><th>supply cut prob</th></tr>
      </thead>
      <tbody>
        <tr><td>Spread1</td><td>Item1</td><td></td><td></td><td></td><td></td><td></td></tr>
        <tr><td>Spread2</td><td>Item2</td><td></td><td></td><td></td><td></td><td></td></tr>
        <tr><td>Spread3</td><td>Item3</td><td></td><td></td><td></td><td></td><td></td></tr>
        <tr><td>Spread4</td><td>Item4</td><td></td><td></td><td></td><td></td><td></td></tr>
        <tr><td>Spread5</td><td>Item5</td><td></td><td></td><td></td><td></td><td></td></tr>
      </tbody>
    </table>

    <h2 class="chart-title supply" style="font-weight:600">Spread vs Supply</h2>
    <h2 class="chart-title time" style="font-weight:600">Spreads across time</h2>

    <svg class="pie" width="124" height="124" viewBox="0 0 124 124" role="img" aria-label="Spread versus supply pie chart">
      <defs>
        <linearGradient id="pieBlue" x1="0" y1="0" x2="1" y2="1"><stop offset="0" stop-color="#a3d9f0"/><stop offset="1" stop-color="#4fbce3"/></linearGradient>
        <linearGradient id="pieOrange" x1="0" y1="0" x2="1" y2="1"><stop offset="0" stop-color="#ffd08a"/><stop offset="1" stop-color="#f58a00"/></linearGradient>
      </defs>
      <circle cx="62" cy="62" r="58" fill="url(#pieBlue)"/>
      <path d="M62 62 L114.5 37.5 A58 58 0 0 1 112.2 91 Z" fill="url(#pieOrange)"/>
      <path d="M62 62 L112.2 91 A58 58 0 0 1 95.3 109.5 Z" fill="#9cd33a"/>
    </svg>

    <svg class="bars" width="340" height="140" viewBox="0 0 340 140" role="img" aria-label="Spreads across time bar chart">
      <line x1="1" y1="0" x2="1" y2="137" stroke="#666" stroke-dasharray="2 2"/>
      <line x1="1" y1="137" x2="336" y2="137" stroke="#666" stroke-dasharray="2 2"/>
      <rect x="46" y="10" width="45" height="127" fill="var(--bar)"/>
      <rect x="119" y="65" width="45" height="72" fill="var(--bar)"/>
      <rect x="187" y="88" width="45" height="49" fill="var(--bar)"/>
    </svg>
  </main>
</body>
</html>
```